Website Online Research Solutions

We are a small European high-tech online research company.
With our own state of the art software we run online panels and are conducting reseach for companies. Partly research via our own panel and partly via panels we maintain for our customers.
Our current website is old and outdatet: www.pravelo.nl.
We are in the process to change the content of the site. We want a modern, european and businesslike design for our new website.
Our logo has to stay the same (left uppersite of our website and attached) but can be changed a little to adapt it to the new design of the website. The colors of the site are up to you.
Target Market(s)
Marketeers and researchers of large and middle size companies in all kind of fields.
Industry/Entity Type
Online
Look and feel
Each slider illustrates characteristics of the customer's brand and the style your logo design should communicate.

```html
<!DOCTYPE html>
<html lang="nl">
<head>
<meta charset="utf-8">
<title>Pravelo – Online Research Solutions</title>
<link href="https://fonts.googleapis.com/css2?family=Arimo:wght@400;700&family=Lora:ital,wght@0,600;1,700&display=swap" rel="stylesheet">
<style>
:root{
  --charcoal:#323436;
  --cyan:#19e2f2;
  --cyan-light:#5ef0fa;
  --teal:#0d6f78;
  --teal-dark:#0a545c;
  --teal-text:#0a4a52;
  --link:#1b9aa6;
  --white:#ffffff;
}
*{margin:0;padding:0;box-sizing:border-box}
html,body{width:895px;height:1200px;overflow:hidden}
body{position:relative;background:var(--cyan);font-family:"Arimo",Arial,sans-serif;color:var(--teal-text)}
.abs{position:absolute}

/* header */
.header{left:0;top:0;width:895px;height:469px;background:var(--charcoal);border-top:2px solid var(--cyan)}
.top-contact{right:91px;top:2px;text-align:right;font-family:"Lora",Georgia,serif;font-size:15px;line-height:17px;color:var(--cyan)}
.brand-name{left:310px;top:56px;font-family:"Lora",Georgia,serif;font-weight:600;font-size:58px;line-height:70px;color:var(--teal)}
.brand-tag{left:310px;top:124px;font-family:"Lora",Georgia,serif;font-weight:600;font-size:37px;line-height:44px;color:var(--teal)}

.nav a{position:absolute;top:190px;height:23px;line-height:23px;text-align:center;background:var(--teal);color:var(--cyan);font-weight:700;font-size:15px;text-decoration:none;border-radius:3px}
.nav a.active{background:var(--cyan);color:var(--teal-dark)}

.intro-title{left:91px;top:244px;width:410px;font-size:14.5px;font-weight:400;line-height:18px;color:var(--cyan)}
.intro-text{left:91px;width:410px;font-size:10px;line-height:14px;color:var(--link);text-align:justify}
.intro-sites{left:91px;top:416px;width:420px;font-size:9.5px;font-weight:700;color:var(--cyan)}
.site-links{left:91px;top:432px;display:flex;gap:14px;font-size:9.5px;color:var(--link)}
.site-links span{border-bottom:1px dotted var(--link)}
.video{left:530px;top:246px;width:274px;height:198px;border-radius:12px;background:var(--cyan);padding:8px}
.video .screen{width:100%;height:100%;border-radius:7px;background:radial-gradient(circle,#8b8d8f,#5f6163);display:flex;align-items:center;justify-content:center}

/* content cards */
.card h3{font-family:"Lora",Georgia,serif;font-style:italic;font-weight:700;font-size:22px;color:var(--teal-dark);text-decoration:underline;line-height:28px}
.card .pic{margin-top:9px;width:208px;height:65px;border-radius:3px;border:2px solid var(--white)}
.card p{margin-top:10px;width:208px;height:65px;overflow:hidden;font-size:10px;line-height:13px;text-align:justify;color:var(--teal-text)}
.card .more{margin:8px 0 0 126px;width:84px;height:25px;border-radius:4px;background:linear-gradient(#3ad0dd,var(--link));color:var(--teal-dark);font-family:"Lora",Georgia,serif;font-style:italic;font-size:13px;text-align:center;line-height:25px}

.box{left:595px;width:208px;background:var(--teal);border:2px solid var(--cyan-light);border-radius:5px;padding:10px 12px;color:var(--cyan)}
.box h3{font-family:"Lora",Georgia,serif;font-style:italic;font-weight:700;font-size:21px;text-decoration:underline;color:var(--cyan)}
.box p{font-size:10px;line-height:13.5px}
.arrows{position:absolute;right:12px;bottom:8px;display:flex;gap:4px}
.arrows span{width:15px;height:15px;background:var(--cyan);color:var(--teal);font-size:11px;font-weight:700;text-align:center;line-height:15px;border-radius:2px}
.map{margin-top:16px;height:46px;background:linear-gradient(135deg,#a7e6ea,#6fc4cb);border-radius:3px}

.steps span{position:absolute;top:946px;height:20px}

/* clients */
.clients{left:0;top:976px;width:895px;height:146px;background:linear-gradient(var(--teal) 0,#0fa9b6 30px,var(--cyan) 32px,var(--cyan))}
.clients h4{position:absolute;left:0;right:0;top:8px;text-align:center;font-family:"Lora",Georgia,serif;font-style:italic;font-weight:700;font-size:17px;color:var(--teal-dark)}
.client-strip{position:absolute;left:144px;top:36px;width:606px;height:92px;background:var(--cyan-light);border-radius:8px}
.client{position:absolute;top:15px;width:93px;height:60px;background:var(--white);border-radius:4px;display:flex;align-items:center;justify-content:center;font-weight:700;font-size:14px;color:var(--teal)}
.round-arrow{position:absolute;top:60px;width:34px;height:34px;border-radius:50%;background:var(--teal);border:2px solid var(--cyan-light)}

.footer{left:0;top:1122px;width:895px;height:78px;background:var(--teal-dark);text-align:center;color:var(--cyan)}
.footer nav{margin-top:25px;font-size:9.5px;word-spacing:3px}
.footer small{display:block;margin-top:4px;font-size:8px}
</style>
</head>
<body>

<header class="abs header">
  <div class="abs top-contact">+31 (0)200 555010<br>info@pravelo.nl</div>
  <div class="abs brand-name">Pravelo</div>
  <div class="abs brand-tag">Online Research Solutions</div>

  <nav class="nav">
    <a class="active" style="left:91px;width:94px">Algemeen</a>
    <a style="left:204px;width:92px">Producten</a>
    <a style="left:317px;width:78px">Demo’s</a>
    <a style="left:409px;width:60px">Media</a>
    <a style="left:488px;width:105px">Referenties</a>
    <a style="left:611px;width:98px">Personeel</a>
    <a style="left:724px;width:80px">Contact</a>
  </nav>

  <h1 class="abs intro-title">Pravelo is gespecialiseerd in online gegevensverzameling en analyse en is werkzaam voor internationale opdrachtgevers.</h1>
  <p class="abs intro-text" style="top:290px">Het bedrijf werd opgericht in 1996 en is gevestigd in Zeedorp, een kleine havenplaats boven Amsterdam. Onze producten zijn ontwikkeld op basis van V, een krachtige en uitermate flexibele onderzoekstool voor het verzamelen &amp; verwerken van researchgegevens. V werd ontwikkeld door opinieonderzoekers vóór opinieonderzoekers.</p>
  <p class="abs intro-text" style="top:358px">Ons team bestaat uit zowel opinieonderzoekers als programmeurs met vele jaren ervaring op het gebied van opinieonderzoek en met name met online toepassingen daarvoor.</p>
  <h2 class="abs intro-sites">Deze bekende sites zijn ontwikkeld en worden beheerd door Pravelo BV:</h2>
  <div class="abs site-links"><span>› www.meetpunt.nl</span><span>› www.stilkamer.nl</span><span>› www.jongmeter.nl</span><span>› Hofmarkt klantenpanel</span></div>

  <div class="abs video">
    <div class="screen" role="img" aria-label="Videospeler">
      <svg width="30" height="30" viewBox="0 0 30 30"><path d="M4 2 L28 15 L4 28 Z" fill="#111"/></svg>
    </div>
  </div>
</header>

<article class="abs card" style="left:91px;top:496px">
  <h3>Dataverzameling</h3>
  <div class="pic" role="img" aria-label="Foto van een enquêteformulier met een computermuis" style="background:linear-gradient(90deg,#e9e9e9,#b9b9b9)"></div>
  <p>Pravelo is uitgegroeid tot een volwaardig speler in de markt met een indrukwekkend portfolio. Zo heeft Pravelo wereldwijd al meer dan 2.000.000 vragenlijsten verwerkt.</p>
  <div class="more">more...</div>
</article>

<article class="abs card" style="left:336px;top:496px">
  <h3>Analyse</h3>
  <div class="pic" role="img" aria-label="Foto van een pen op een analyseoverzicht" style="background:linear-gradient(90deg,#f2f2f2,#a9a9a9)"></div>
  <p>Vervolgens kan tijdens de veldwerkperiode een online analyse worden gemaakt van realtime data. Het is mogelijk de gegevens tijdens het veldwerk gewogen te presenteren.</p>
  <div class="more">more...</div>
</article>

<article class="abs card" style="left:91px;top:735px">
  <h3>Datasetpublising</h3>
  <div class="pic" role="img" aria-label="Foto van een rennend dier in zwart-wit" style="background:linear-gradient(90deg,#9a9a9a,#d8d8d8,#8a8a8a)"></div>
  <p>U kunt per gebruiker, die u zelf kunt aanmaken, instellen welk deel van uw dataset deze mag zien: u kunt het aantal variabelen beperken of een filter instellen.</p>
  <div class="more">more...</div>
</article>

<article class="abs card" style="left:336px;top:735px">
  <h3>Panel: inPoll</h3>
  <div class="pic" role="img" aria-label="Illustratie van een vogel naast een panelkeurmerk" style="background:linear-gradient(90deg,#ffffff,#d9dde0)"></div>
  <p>Pravelo beschikt over een zeer uitgebreid panel met meer dan 50000 deelnemers. Dit panel heet inPoll en wordt beheerd met een geavanceerd panel-systeem.</p>
  <div class="more">more...</div>
</article>

<aside class="abs box" style="top:502px;height:204px">
  <h3>Testimonials</h3>
  <p style="margin-top:10px;text-align:justify">“Het is een verademing om met Pravelo te werken in vergelijking met andere onderzoeksbureaus. Je hoeft iets maar één keer uit te leggen, ze denken op een goede en prettige manier mee en de kwaliteit is prima in orde. Ik ben, kortom, zeer tevreden.”</p>
  <p style="margin-top:9px;font-style:italic;font-size:9.5px">Marieke de Wit - Research Director MerkLijn</p>
  <div class="arrows"><span>∧</span><span>∨</span></div>
</aside>

<aside class="abs box" style="top:737px;height:205px">
  <h3>Contact</h3>
  <p style="margin-top:8px">Pravelo BV<br>Havenstraat 12<br>1141 AB Zeedorp<br><i>tel: +31 (0)200 555010<br>fax: +31 (0)200 555019<br>email: <u>info@pravelo.nl</u></i></p>
  <div class="map" role="img" aria-label="Kaart met de bedrijfslocatie"></div>
</aside>

<div class="steps">
  <span style="left:0;width:55px;background:var(--charcoal)"></span>
  <span style="left:55px;width:20px;background:var(--teal)"></span>
  <span style="left:75px;width:22px;background:#0fa9b6"></span>
  <span style="left:97px;width:20px;background:var(--cyan-light)"></span>
</div>

<section class="abs clients">
  <h4>Our Clients</h4>
  <div class="round-arrow" style="left:100px"><svg width="30" height="30" viewBox="0 0 30 30"><path d="M12 9 L18 15 L12 21" stroke="#19e2f2" stroke-width="3" fill="none"/></svg></div>
  <div class="client-strip">
    <div class="client" style="left:9px">Velden</div>
    <div class="client" style="left:109px">Kroon</div>
    <div class="client" style="left:209px">Hofmarkt</div>
    <div class="client" style="left:309px">Brantwise</div>
    <div class="client" style="left:409px">Umara</div>
    <div class="client" style="left:505px">Vormhuis</div>
  </div>
  <div class="round-arrow" style="left:759px"><svg width="30" height="30" viewBox="0 0 30 30"><path d="M18 9 L12 15 L18 21" stroke="#19e2f2" stroke-width="3" fill="none"/></svg></div>
</section>

<footer class="abs footer">
  <nav>Algemeen | Producten | Demo’s | Media | Referenties | Personeel | Contact</nav>
  <small>Copyright © 2010 Pravelo. All Rights Reserved.</small>
</footer>

</body>
</html>
```